Candy gift box

I want a fun design like the attachments with my company name on it. I want to use this box to hold small plastic 2x2x2 containers of candy. So I need this box to be the wow factor and something unique. Box size is 10.125x6.5x2.75. I would also like it to have maybe a few fun words and even a dots on top would also like to fun bright colour for inside the flap. Company name is Tartloop.

Requirements
Nice to have
• Bright fun colours even dots or confetti

```html
<!DOCTYPE html>
<html lang="en">
<head>
<meta charset="utf-8">
<title>Tartloop candy gift box – top and bottom panels</title>
<link rel="stylesheet" href="https://fonts.googleapis.com/css2?family=Great+Vibes&family=Tinos:wght@700&display=swap">
<style>
  :root {
    --page: #ffffff;
    --box-pink: #e7609f;
    --ink-light: #ffffff;
    --label: #555555;
    --confetti-yellow: #f7d84a;
    --confetti-blue: #4fb6e8;
    --confetti-green: #7cc96a;
    --confetti-orange: #f39a3c;
    --confetti-purple: #9b6fd0;
    --confetti-red: #e8414f;
  }
  * { margin: 0; padding: 0; box-sizing: border-box; }
  html, body { width: 800px; height: 1200px; overflow: hidden; background: var(--page); }
  .sheet { position: relative; width: 800px; height: 1200px; }

  .panel {
    position: absolute;
    left: 100px;
    width: 600px;
    background: var(--box-pink);
    overflow: hidden;
  }
  .panel--top { top: 14px; height: 358px; }
  .panel--bottom { top: 418px; height: 448px; }

  .panel-label {
    position: absolute;
    left: 72px;
    font-family: Arial, sans-serif;
    font-size: 11px;
    color: var(--label);
    transform: rotate(-90deg);
    transform-origin: left top;
    letter-spacing: 0.5px;
  }
  .panel-label--top { top: 212px; }
  .panel-label--bottom { top: 660px; }

  .confetti-area {
    position: absolute;
    background: linear-gradient(120deg,
      var(--confetti-yellow) 0%, var(--confetti-orange) 18%,
      var(--confetti-blue) 36%, var(--confetti-green) 54%,
      var(--confetti-purple) 72%, var(--confetti-red) 88%, var(--confetti-yellow) 100%);
  }
  .confetti-area--corner {
    left: 0; top: 0; width: 380px; height: 160px;
    -webkit-mask-image: radial-gradient(ellipse 100% 100% at 0 0, #000 45%, transparent 100%);
            mask-image: radial-gradient(ellipse 100% 100% at 0 0, #000 45%, transparent 100%);
  }
  .confetti-area--corner-right {
    right: 0; bottom: 0; width: 340px; height: 150px;
    -webkit-mask-image: radial-gradient(ellipse 100% 100% at 100% 100%, #000 40%, transparent 100%);
            mask-image: radial-gradient(ellipse 100% 100% at 100% 100%, #000 40%, transparent 100%);
  }
  .confetti-area--band {
    left: 0; bottom: 0; width: 600px; height: 110px;
    background: linear-gradient(90deg,
      var(--confetti-yellow), var(--confetti-blue), var(--confetti-green),
      var(--confetti-orange), var(--confetti-purple), var(--confetti-red), var(--confetti-yellow));
    -webkit-mask-image: linear-gradient(180deg, transparent 0%, #000 55%);
            mask-image: linear-gradient(180deg, transparent 0%, #000 55%);
  }

  .brand-name {
    position: absolute;
    left: 0; right: 0;
    font-family: "Great Vibes", cursive;
    color: var(--ink-light);
    font-weight: 400;
    text-align: center;
    line-height: 1;
    white-space: nowrap;
  }
  .panel--top .brand-name { top: 140px; font-size: 118px; }
  .panel--bottom .brand-name { top: 30px; font-size: 68px; }

  .product-copy {
    position: absolute;
    left: 72px; right: 72px; top: 120px;
    font-family: "Tinos", serif;
    font-weight: 700;
    font-size: 13.5px;
    line-height: 1.45;
    color: var(--ink-light);
    text-align: center;
  }
</style>
</head>
<body>
<main class="sheet">
  <span class="panel-label panel-label--top">top</span>
  <section class="panel panel--top">
    <div class="confetti-area confetti-area--corner" role="img" aria-label="Scattered bright confetti dots"></div>
    <div class="confetti-area confetti-area--corner-right" role="img" aria-label="Scattered bright confetti dots"></div>
    <h1 class="brand-name">Tartloop</h1>
  </section>

  <span class="panel-label panel-label--bottom">bottom</span>
  <section class="panel panel--bottom">
    <h2 class="brand-name">Tartloop</h2>
    <p class="product-copy">Every box is packed by hand with bright little treats, chewy, fizzy and sweet. Open the lid, pick a cube and share the fun with friends. Our candy is made in small batches with real fruit flavours and a whole lot of colour. Keep cool and dry, enjoy within four weeks of opening. Made with love for every sweet tooth out there, from tiny nibbles to big happy handfuls of joy.</p>
    <div class="confetti-area confetti-area--band" role="img" aria-label="Band of bright confetti dots"></div>
  </section>
</main>
</body>
</html>
```